New Poster Design for Film Festival

Hi! We need a poster design for our student film festival and the Harlow Ridge University. We screen over 300 short films over a 3 days in May. Our committee wants a look feel similar to the image we attached below.

Target Market(s)

Students and general audience.

Industry/Entity Type

Festival

Colors
3377b5
85abd2
34b8a4
f68e4e

Requirements
Must have
• Otters Film Festival
17th Annual
May 2-3-4 2014
Ned Varrow Cinema
Free Admission
Department of Screen and Digital Narrative

Poster size 36" (high) x 24" (wide)
Harlow Ridge University
www.ottersfilmfest.example
Nice to have
• Bold lettering
Should not have
• Flamingos - hate them :)

```html
<!DOCTYPE html>
<html lang="en">
<head>
<meta charset="utf-8">
<title>300 in 3 — Otters Film Festival</title>
<link rel="stylesheet" href="https://fonts.googleapis.com/css2?family=Ultra&family=Alfa+Slab+One&family=League+Gothic&family=Oswald:wght@500;600&display=block">
<style>
  :root {
    --festival-blue: #3377b5;
    --sky-blue: #85abd2;
    --teal: #34b8a4;
    --orange: #f68e4e;
    --white: #ffffff;
    --ink: #1d2a36;
    --edge: #1c4f7a;
  }
  html, body {
    margin: 0;
    padding: 0;
    width: 800px;
    height: 1200px;
    overflow: hidden;
    background: var(--festival-blue);
  }
  .poster {
    display: block;
    width: 800px;
    height: 1200px;
  }
  .poster-ground { fill: var(--festival-blue); stroke: var(--edge); stroke-width: 2; }
  .film-strip { fill: url(#sprocket-holes); stroke: var(--ink); stroke-width: 1.5; }
  .headline, .tagline, .date-year, .venue, .host-name {
    font-family: "Ultra", "Alfa Slab One", serif;
    font-weight: 400;
  }
  .headline, .tagline { fill: var(--orange); }
  .edition, .festival-name { font-family: "League Gothic", "Oswald", sans-serif; fill: var(--sky-blue); }
  .date-year { fill: var(--teal); }
  .date-month, .date-days { font-family: "Oswald", sans-serif; font-weight: 500; fill: var(--teal); }
  .venue { fill: var(--teal); }
  .host-mark { fill: var(--white); }
  .host-name { fill: var(--white); }
  .website { font-family: "Oswald", sans-serif; font-weight: 600; fill: var(--teal); letter-spacing: 0.5px; }
</style>
</head>
<body>
<svg class="poster" viewBox="0 0 800 1200" xmlns="http://www.w3.org/2000/svg">
  <defs>
    <pattern id="sprocket-holes" width="10.5" height="14" patternUnits="userSpaceOnUse">
      <rect width="10.5" height="14" fill="#ffffff"/>
      <rect x="0" y="0" width="1.4" height="14" fill="#1d2a36"/>
    </pattern>
  </defs>

  <rect class="poster-ground" x="1" y="1" width="798" height="1198"/>

  <rect class="film-strip" x="22" y="21" width="748" height="13"/>

  <text class="headline" x="18" y="298" font-size="300" textLength="762" lengthAdjust="spacingAndGlyphs">300</text>
  <text class="headline" x="30" y="585" font-size="300" textLength="732" lengthAdjust="spacingAndGlyphs">IN3</text>
  <text class="tagline" x="52" y="640" font-size="38" textLength="693" lengthAdjust="spacingAndGlyphs">300 + FILMS IN 3 DAYS</text>

  <rect class="film-strip" x="28" y="655" width="737" height="13"/>

  <text class="edition" x="40" y="850" font-size="222" textLength="512" lengthAdjust="spacingAndGlyphs">17TH ANNUAL</text>

  <g class="festival-dates">
    <text class="date-year" x="597" y="730" font-size="46" text-anchor="middle">2</text>
    <text class="date-year" x="597" y="768" font-size="46" text-anchor="middle">0</text>
    <text class="date-year" x="597" y="806" font-size="46" text-anchor="middle">1</text>
    <text class="date-year" x="597" y="844" font-size="46" text-anchor="middle">4</text>
    <text class="date-month" x="653" y="738" font-size="56" text-anchor="middle">M</text>
    <text class="date-month" x="653" y="790" font-size="56" text-anchor="middle">A</text>
    <text class="date-month" x="653" y="842" font-size="56" text-anchor="middle">Y</text>
    <text class="date-days" x="685" y="738" font-size="56" textLength="80" lengthAdjust="spacingAndGlyphs">2ND</text>
    <text class="date-days" x="685" y="790" font-size="56" textLength="80" lengthAdjust="spacingAndGlyphs">3RD</text>
    <text class="date-days" x="685" y="842" font-size="56" textLength="80" lengthAdjust="spacingAndGlyphs">4TH</text>
  </g>

  <text class="festival-name" x="40" y="1005" font-size="190" textLength="730" lengthAdjust="spacingAndGlyphs">OTTERS FILM FESTIVAL</text>

  <text class="venue" x="45" y="1058" font-size="30" textLength="723" lengthAdjust="spacingAndGlyphs">NED VARROW CINEMA</text>
  <text class="venue" x="135" y="1095" font-size="30" textLength="545" lengthAdjust="spacingAndGlyphs">FREE ADMISSION</text>

  <g class="host">
    <rect class="host-mark" x="60" y="1118" width="93" height="60"/>
    <text class="host-name" x="170" y="1132" font-size="14" textLength="272" lengthAdjust="spacingAndGlyphs">HARLOW RIDGE UNIVERSITY</text>
    <text class="host-name" x="170" y="1157" font-size="18" textLength="392" lengthAdjust="spacingAndGlyphs">DEPARTMENT OF SCREEN</text>
    <text class="host-name" x="170" y="1177" font-size="18" textLength="350" lengthAdjust="spacingAndGlyphs">&amp; DIGITAL NARRATIVE</text>
  </g>

  <text class="website" x="768" y="1177" font-size="17" text-anchor="end" textLength="186" lengthAdjust="spacingAndGlyphs">www.ottersfilmfest.example</text>
</svg>
</body>
</html>
```